Wren Vehicle Polishing (Mobile detail)

I need a business card made up. I'd like it to be different in some form, either raised, embossed, debossed, something cool that stands out. (preferably embossed text somewhere in it). I will be including the Initial png file. Let me know if you need the photoshop of adobe illustrator file to work with.

Information to be included: Text: XXX-XXX-XXXX Phone: XXX-XXX-XXXX Email: wrenpolishcrew@mailbox-demo.net Website: www.socialpage-demo.net/wrenpolishKTR Hours of operation: Mon - Fri 7:00AM to 8:00PM Sat - 10:00AM to 8:00PM

Target Market(s)

Mobile automotive detailing

Industry/Entity Type

Automotive

Contact Information for Business Card

Make it stand out with embossed lettering, I'd also like the background to be glossy black or matte, something that represents a shiny car, black preferred

Requirements
Must have
• A glossy background, or something.
• My logo, pick one of them that best fits your design.
Should not have
• White background,
• something that does not stand out.

```html
<!DOCTYPE html>
<html lang="en">
<head>
<meta charset="utf-8">
<title>Wren Vehicle Polishing – Business Card</title>
<link rel="stylesheet" href="https://fonts.googleapis.com/css2?family=Open+Sans:wght@400;600&display=swap">
<style>
  :root {
    --stage: #3a3a3a;
    --card-black: #070707;
    --card-gloss: #1c1c1c;
    --orange-deep: #c8701c;
    --orange-text: #e07a22;
    --silver-dark: #9a9a9a;
    --ink: #1a1206;
    --text-light: #f2f2f2;
    --text-muted: #bdbdbd;
  }
  html, body {
    margin: 0;
    width: 1200px;
    height: 780px;
    overflow: hidden;
    background: var(--stage);
    font-family: "Open Sans", Arial, sans-serif;
  }
  .card {
    position: absolute;
    left: 100px;
    top: 104px;
    width: 1000px;
    height: 572px;
    background: radial-gradient(ellipse at 65% 20%, var(--card-gloss) 0%, var(--card-black) 60%);
    overflow: hidden;
    box-shadow: 0 12px 30px rgba(0,0,0,.5);
  }
  .card-swoosh {
    position: absolute;
    inset: 0;
  }
  .brand {
    position: absolute;
    left: 560px;
    top: 60px;
    display: flex;
    align-items: center;
    gap: 20px;
  }
  .brand-mark {
    width: 86px;
    height: 86px;
    border-radius: 50%;
    background: var(--silver-dark);
  }
  .brand-name {
    color: var(--text-light);
    font-weight: 600;
    font-size: 34px;
    line-height: 1.15;
    width: 260px;
  }
  .person {
    position: absolute;
    left: 70px;
    top: 175px;
  }
  .person-name {
    margin: 0;
    color: var(--orange-text);
    font-weight: 400;
    font-size: 38px;
    line-height: 1.3;
    letter-spacing: .5px;
    text-transform: uppercase;
  }
  .person-role {
    margin: 0;
    color: var(--text-muted);
    font-size: 26px;
    line-height: 1.3;
  }
  .contacts {
    position: absolute;
    left: 70px;
    top: 272px;
    margin: 0;
    padding: 0;
    list-style: none;
  }
  .contact-item {
    display: flex;
    align-items: center;
    gap: 14px;
    height: 36px;
    color: var(--text-light);
    font-size: 22px;
    white-space: nowrap;
  }
  .contact-icon {
    width: 26px;
    height: 26px;
    flex: none;
    background: var(--orange-deep);
    display: flex;
    align-items: center;
    justify-content: center;
  }
</style>
</head>
<body>
  <section class="card">
    <svg class="card-swoosh" width="1000" height="572" viewBox="0 0 1000 572">
      <defs>
        <linearGradient id="band-orange" x1="0" y1="0" x2="0" y2="1">
          <stop offset="0" stop-color="#f0a640"/>
          <stop offset="1" stop-color="#d97f22"/>
        </linearGradient>
        <linearGradient id="band-silver" x1="0" y1="0" x2="1" y2="0">
          <stop offset="0" stop-color="#8a8a8a"/>
          <stop offset=".5" stop-color="#f4f4f4"/>
          <stop offset="1" stop-color="#bcbcbc"/>
        </linearGradient>
        <path id="hours-line" d="M40 548 C 340 566, 650 496, 980 318" fill="none"/>
      </defs>
      <path class="silver-stripe" d="M0 440 C 300 470, 650 390, 1000 200 L 1000 232 C 650 422, 300 502, 0 476 Z" fill="url(#band-silver)"/>
      <path class="orange-band" d="M0 490 C 300 518, 650 438, 1000 250 L 1000 572 L 0 572 Z" fill="url(#band-orange)"/>
      <path d="M0 484 C 300 512, 650 432, 1000 243" stroke="#000" stroke-width="8" fill="none"/>
      <text class="hours" fill="var(--ink)" font-family="Open Sans, Arial, sans-serif" font-size="25" font-weight="600">
        <textPath href="#hours-line" startOffset="17%">Mon - Fri 7:00AM to 8:00PM Sat - 10:00AM to 8:00PM</textPath>
      </text>
    </svg>

    <div class="brand">
      <div class="brand-mark"></div>
      <div class="brand-name">Wren Vehicle Polishing</div>
    </div>

    <div class="person">
      <h1 class="person-name">Employee Name</h1>
      <p class="person-role">Owner</p>
    </div>

    <ul class="contacts">
      <li class="contact-item">
        <span class="contact-icon">
          <svg width="14" height="18" viewBox="0 0 14 18"><rect x="1" y="1" width="12" height="16" rx="2" fill="none" stroke="#000" stroke-width="2"/><rect x="4" y="4" width="6" height="7" fill="#000"/></svg>
        </span>
        000-000-0000
      </li>
      <li class="contact-item">
        <span class="contact-icon">
          <svg width="18" height="14" viewBox="0 0 18 14"><rect x="1" y="1" width="16" height="12" fill="none" stroke="#000" stroke-width="2"/><path d="M1 1 L9 8 L17 1" fill="none" stroke="#000" stroke-width="2"/></svg>
        </span>
        wrenpolishcrew@mailbox-demo.net
      </li>
      <li class="contact-item">
        <span class="contact-icon">
          <svg width="18" height="18" viewBox="0 0 18 18"><circle cx="9" cy="9" r="7.5" fill="none" stroke="#000" stroke-width="2"/><ellipse cx="9" cy="9" rx="3.5" ry="7.5" fill="none" stroke="#000" stroke-width="1.5"/><path d="M1.5 9 H16.5" stroke="#000" stroke-width="1.5"/></svg>
        </span>
        www.socialpage-demo.net/wrenpolishKTR
      </li>
    </ul>
  </section>
</body>
</html>
```